Real Estate Company Website

We are working with TZ Real Estate and building a new website for them.
Some sites to use for content/competitors and inspiration:
https://lucettabrom.zp.com
https://www.hovelnest.com
https://www.keystrand88.com
https://tobinahaldreth.com
https://pollyvestrum.com
https://oswinbrakel.com
https://marcotuzzlegroup.com
Thank you for taking the time to consider designing a website for us. We are web developers based in Stockton, CA, USA. Most of our projects go through the same process. Understanding this process may help you win a project with us. We custom-code all of our websites in-house. We don’t have any requirements as to what tools you use for your design, but we prefer Figma files. For any design that we label as four stars, we send it to the client for review. The client picks the final design they want us to use. Once we complete this process, we will continue to show additional clients all the four-star sites and purchase them later. Your designs will have multiple chances to sell. For better chances of success, we ask that you follow these guidelines.
IMAGES:
If you use any images or icons in the design, we ask that you have a link to the asset so we can purchase the image/icon. Most of the designs we submit do not have the customer’s images on them unless they have some great images. Be creative; show us the feeling you are trying to portray with your image choices. Use any royalty-free site you choose. We subscribe to Plenvo and mainly use their images, but we can purchase images outside of Plenvo. PLEASE NOTE: we will not submit designs to clients with watermarks on the images.
FONTS:
We ask that you identify the fonts used in the design. This can be done in a message if you want. We typically use Google Fonts and Plenvo Fonts.
CONTENT:
We're always open to different content and ideas. We often submit designs with stock images so the client can see our vision. We typically take pictures after the website launch to use their images with our vision. Lorem Ipsum is fine for paragraphs, but we ask that you write the headers in correct English. We want to be able to show the vision and identify the sections of the website.
INSPIRATION:
We typically add a couple of links in the brief of websites we like to help you get started in your design.
REVISIONS:
We do not often ask for revisions of the designs unless we see something in the design that may not appeal to the client. If there are slight changes that we want to make, we do that in the development process.
FEEDBACK:
We rarely give feedback on designs during the design process. We are working on many website projects and do not have the time to provide feedback. We usually respond if your request is well thought out and asks specific questions, but a note asking “feedback, please” usually goes unanswered.

```html
<!DOCTYPE html>
<html lang="en">
<head>
<meta charset="utf-8">
<title>TZ Real Estate</title>
<link href="https://fonts.googleapis.com/css2?family=Lora:wght@400;500&family=Inter:wght@400;500;600&display=swap" rel="stylesheet">
<style>
:root{
  --teal:#1d6a80;
  --teal-dark:#0f5467;
  --teal-deep:#134a5a;
  --ink:#1c2226;
  --muted:#7b868c;
  --line:#e2e8eb;
  --pale:#eef8fb;
  --white:#ffffff;
}
*{box-sizing:border-box;margin:0;padding:0}
html,body{width:1200px;height:5124px;overflow:hidden}
body{font-family:"Inter",sans-serif;color:var(--ink);background:var(--white);position:relative}
.serif{font-family:"Lora",serif;font-weight:400}
section,header,footer{position:absolute;left:0;width:1200px}
.abs{position:absolute}

/* hero */
.hero{top:0;height:656px;background:linear-gradient(160deg,#4d8e9c 0%,#2f7282 45%,#3d8290 100%)}
.hero-photo{position:absolute;inset:0;background:radial-gradient(ellipse at 55% 25%,rgba(170,205,210,.45),transparent 55%),radial-gradient(ellipse at 15% 80%,rgba(20,70,60,.55),transparent 50%),radial-gradient(ellipse at 85% 75%,rgba(25,80,70,.5),transparent 50%)}
.logo{position:absolute;left:28px;top:26px;color:var(--white);font-family:"Lora",serif;font-size:22px;display:flex;align-items:center;gap:10px}
.logo i{width:14px;height:14px;border-radius:50%;background:var(--white);display:block}
.nav{position:absolute;left:408px;top:28px;display:flex;gap:34px;font-size:13px;color:var(--white);font-weight:500}
.nav .active{border-bottom:2px solid var(--white);padding-bottom:6px}
.phone{position:absolute;left:888px;top:28px;color:var(--white);font-size:13px;font-weight:500;display:flex;gap:6px;align-items:center}
.btn-outline-w{position:absolute;left:1032px;top:18px;width:142px;height:38px;border:2px solid var(--white);border-radius:20px;color:var(--white);font-size:13px;font-weight:500;display:flex;align-items:center;justify-content:center}
.hero-kicker{position:absolute;top:174px;width:100%;text-align:center;color:var(--white);font-size:21px}
.hero-title{position:absolute;top:214px;width:100%;text-align:center;color:var(--white);font-size:72px;line-height:84px}
.search{position:absolute;left:246px;top:416px;width:710px;height:62px;background:var(--white);border-radius:31px;display:flex;align-items:center;padding-left:28px;gap:12px;color:#9aa3a8;font-size:13px}
.search .go{position:absolute;right:8px;top:8px;width:164px;height:46px;border-radius:23px;background:var(--teal-dark);color:var(--white);font-size:14px;font-weight:500;display:flex;align-items:center;justify-content:center}
.tabs{position:absolute;top:498px;left:0;width:100%;display:flex;justify-content:center;gap:40px;color:var(--white);font-size:13px;font-weight:600}
.tabs .on{border-bottom:2px solid var(--white);padding-bottom:6px}

/* intro */
.kicker{color:var(--teal);font-size:17px;text-align:center}
.h2{font-size:33px;text-align:center}
.lead{font-size:13px;line-height:26px;color:var(--muted);text-align:center}
.intro{top:656px;height:850px}
.service{position:absolute;top:286px;width:340px;height:340px;border-radius:8px;overflow:hidden}
.service .ph{position:absolute;inset:0}
.service span{position:absolute;bottom:24px;width:100%;text-align:center;color:var(--white);font-family:"Lora",serif;font-size:22px}
.stat{position:absolute;top:702px;width:250px;height:106px;background:var(--pale);border-radius:8px;display:flex;align-items:center;padding-left:26px;gap:22px}
.stat b{font-family:"Lora",serif;font-weight:400;font-size:27px;color:var(--teal);display:block}
.stat small{font-size:12px;font-weight:500}

/* featured */
.featured{top:1506px;height:684px}
.sec-title{position:absolute;left:66px;font-size:33px}
.arrows{position:absolute;display:flex;gap:10px}
.arrows span{width:32px;height:32px;border:1px solid #b9c3c8;border-radius:4px;display:flex;align-items:center;justify-content:center}
.card{position:absolute;width:340px;border:1px solid var(--line);border-radius:8px;overflow:hidden;background:var(--white)}
.card .ph{height:224px;position:relative}
.price{position:absolute;right:14px;top:16px;background:var(--teal-dark);color:var(--white);font-size:13px;font-weight:600;padding:9px 16px;border-radius:5px}
.card .loc{font-size:13px;color:var(--muted);margin:22px 0 0 16px}
.card h3{font-family:"Lora",serif;font-weight:400;font-size:22px;margin:10px 16px 0}
.card .meta{font-size:12px;color:var(--muted);margin:12px 16px 0}
.card .row{display:flex;justify-content:space-between;margin:28px 16px 26px}
.tag{background:var(--pale);color:var(--teal);font-size:13px;padding:10px 22px;border-radius:5px}
.pill{border:1.5px solid var(--teal);color:var(--teal);font-size:13px;padding:9px 20px;border-radius:20px}

/* testimonials */
.testimonials{top:2190px;height:468px;background:linear-gradient(100deg,#2e7386 0%,#3c8395 55%,#2d6f80 100%)}
.testimonials .ph{position:absolute;inset:0;background:radial-gradient(ellipse at 78% 40%,rgba(140,185,195,.35),transparent 60%)}
.t-kicker{position:absolute;left:66px;top:108px;color:var(--white);font-size:18px}
.t-title{position:absolute;left:66px;top:146px;color:var(--white);font-size:41px;line-height:51px}
.t-arrows{position:absolute;left:66px;top:322px;display:flex;gap:10px}
.t-arrows span{width:32px;height:32px;border:1px solid var(--white);border-radius:4px;display:flex;align-items:center;justify-content:center}
.avatar{position:absolute;left:512px;top:108px;width:82px;height:82px;border-radius:50%;background:linear-gradient(150deg,#e9e4df,#b7a79a);border:3px solid var(--white)}
.quote{position:absolute;left:512px;top:218px;width:620px;color:var(--white);font-size:22px;line-height:34px}
.q-by{position:absolute;left:512px;top:338px;color:var(--white);font-size:13px;font-weight:600}

/* blog */
.blog{top:2658px;height:770px}
.view-all{position:absolute;left:982px;top:118px;border:1.5px solid var(--teal);color:var(--teal);font-size:13px;padding:9px 26px;border-radius:20px}
.blog .card .ph{height:226px}
.cat{font-size:12px;color:var(--muted);letter-spacing:.5px;margin:24px 0 0 16px;font-weight:500}
.blog .card h3{font-size:22px;line-height:29px;margin-top:8px}
.excerpt{font-size:13px;line-height:24px;color:var(--muted);margin:12px 16px 0}
.blog .pill{display:inline-block;margin:22px 16px 26px}

/* video */
.video{top:3428px;height:828px;background:linear-gradient(var(--pale) 0,var(--pale) 440px,var(--white) 440px)}
.player{position:absolute;left:66px;top:199px;width:1068px;height:530px;background:linear-gradient(90deg,#3f6a3a 0%,#4f7d44 30%,#6c7f83 55%,#5d7478 80%,#4f7548 100%)}
.play{position:absolute;left:484px;top:216px;width:96px;height:96px;border-radius:50%;background:var(--white);display:flex;align-items:center;justify-content:center}

/* newsletter */
.newsletter{top:4256px;height:328px}
.email{position:absolute;left:332px;top:204px;width:536px;height:64px;border:1.5px solid #c9d3d7;border-radius:32px;display:flex;align-items:center;padding-left:24px;gap:10px;color:var(--muted);font-size:13px}
.email .go{position:absolute;right:8px;top:8px;width:164px;height:46px;border-radius:23px;background:var(--teal-dark);color:var(--white);font-size:13px;font-weight:600;display:flex;align-items:center;justify-content:center}

/* footer */
.footer{top:4584px;height:540px;background:var(--pale)}
.f-logo{position:absolute;left:72px;top:130px;font-family:"Lora",serif;font-size:30px;color:var(--teal-deep);display:flex;align-items:center;gap:12px}
.f-logo i{width:20px;height:20px;border-radius:50%;background:var(--teal-deep);display:block}
.f-col{position:absolute;top:92px}
.f-col h4{font-size:13px;font-weight:500;letter-spacing:.5px;margin-bottom:20px}
.f-col p{font-family:"Lora",serif;font-size:16px;line-height:26px;color:var(--teal)}
.f-col p+p{margin-top:10px}
.social{display:flex;gap:12px}
.social span{width:36px;height:36px;border-radius:50%;background:var(--teal-dark);display:block}
.f-rule{position:absolute;left:66px;top:282px;width:1068px;border-top:1px solid #d5e1e5}
.legal{position:absolute;left:66px;top:314px;font-size:14px;color:var(--teal)}
.legal em{font-style:normal;color:var(--ink);margin:0 4px}
.f-text{position:absolute;left:66px;top:364px;width:1068px;font-size:13px;line-height:24px;color:var(--muted)}
.copy{position:absolute;left:66px;top:498px;font-size:13px;color:var(--muted)}
</style>
</head>
<body>

<header class="hero">
  <div class="hero-photo" role="img" aria-label="Aerial view of a large modern home surrounded by lush trees, tinted teal"></div>
  <div class="logo"><i></i>TZ Real Estate</div>
  <nav class="nav"><span class="active">Home</span><span>About Us</span><span>Properties</span><span>Agents</span><span>Blog</span></nav>
  <div class="phone">
    <svg width="13" height="13" viewBox="0 0 24 24" fill="#fff"><path d="M6.6 10.8a15.1 15.1 0 0 0 6.6 6.6l2.2-2.2a1 1 0 0 1 1-.25 11.4 11.4 0 0 0 3.6.6 1 1 0 0 1 1 1V20a1 1 0 0 1-1 1A17 17 0 0 1 3 4a1 1 0 0 1 1-1h3.5a1 1 0 0 1 1 1c0 1.25.2 2.45.6 3.6a1 1 0 0 1-.25 1z"/></svg>
    (555) 014 2298
  </div>
  <div class="btn-outline-w">Contact Us</div>
  <div class="hero-kicker">With TZ Real Estate</div>
  <h1 class="hero-title serif">Discover Your Next<br>Home in California</h1>
  <div class="search">
    <svg width="16" height="16" viewBox="0 0 24 24" fill="none" stroke="#1d6a80" stroke-width="3"><circle cx="10" cy="10" r="7"/><path d="M15 15l6 6"/></svg>
    Search properties
    <div class="go">Search Now</div>
  </div>
  <div class="tabs"><span class="on">BUY</span><span>SELL</span><span>RENT</span></div>
</header>

<section class="intro">
  <div class="abs kicker" style="top:94px;width:100%">TZ Real Estate</div>
  <h2 class="abs h2 serif" style="top:128px;width:100%">California's #1 Real Estate Company</h2>
  <p class="abs lead" style="top:180px;left:150px;width:900px">Undas obliquis effigiem amphitrite. Valles hanc. Nubes dominari imagine! Caeleste grandia densior peregrinum regio. Cesserunt caelumque. Vultus quae litem. Coercuit caeli sublime. Finxit ventis caelo rapidisque. Poena orba congeriem. Lumina umor partim hunc tepescunt! Iapeto mutatas dei duris quisquis nitidis erant terra militis.</p>

  <div class="service" style="left:66px"><div class="ph" role="img" aria-label="Kitchen with dark wood cabinets and bar stools" style="background:linear-gradient(180deg,#c9b9a6 0%,#7a5a44 55%,#3a2a20 100%)"></div><span>Buy Properties</span></div>
  <div class="service" style="left:430px"><div class="ph" role="img" aria-label="Bright living room with grey sofa" style="background:linear-gradient(180deg,#d9d6cf 0%,#9f968a 55%,#4f4a44 100%)"></div><span>Sell Properties</span></div>
  <div class="service" style="left:795px"><div class="ph" role="img" aria-label="White kitchen with pendant lights" style="background:linear-gradient(180deg,#eeecea 0%,#b9b4ad 55%,#5a5550 100%)"></div><span>Rent Properties</span></div>

  <div class="stat" style="left:66px"><svg width="30" height="30" viewBox="0 0 24 24" fill="none" stroke="#1d6a80" stroke-width="1.6"><path d="M3 11l9-7 9 7"/><path d="M5 10v10h14V10"/><path d="M10 20v-6h4v6"/></svg><div><b>$389M</b><small>Total Sales in 2023</small></div></div>
  <div class="stat" style="left:339px"><svg width="30" height="30" viewBox="0 0 24 24" fill="none" stroke="#1d6a80" stroke-width="1.6"><path d="M3 11l9-7 9 7"/><path d="M5 10v10h14V10"/><path d="M10 20v-6h4v6"/></svg><div><b>$2,000M</b><small>in Career Sales</small></div></div>
  <div class="stat" style="left:612px"><svg width="30" height="30" viewBox="0 0 24 24" fill="none" stroke="#1d6a80" stroke-width="1.6"><path d="M3 11l9-7 9 7"/><path d="M5 10v10h14V10"/><path d="M10 20v-6h4v6"/></svg><div><b>20+</b><small>Qualified Agents</small></div></div>
  <div class="stat" style="left:884px"><svg width="30" height="30" viewBox="0 0 24 24" fill="none" stroke="#1d6a80" stroke-width="1.6"><path d="M3 11l9-7 9 7"/><path d="M5 10v10h14V10"/><path d="M10 20v-6h4v6"/></svg><div><b>1,000+</b><small>Happy Customers</small></div></div>
</section>

<section class="featured">
  <h2 class="sec-title serif" style="top:74px">Featured Properties in Your Area</h2>
  <div class="arrows" style="left:1054px;top:78px">
    <span><svg width="10" height="10" viewBox="0 0 10 10" fill="none" stroke="#555" stroke-width="1.5"><path d="M6.5 1.5L3 5l3.5 3.5"/></svg></span>
    <span><svg width="10" height="10" viewBox="0 0 10 10" fill="none" stroke="#555" stroke-width="1.5"><path d="M3.5 1.5L7 5 3.5 8.5"/></svg></span>
  </div>

  <div class="card" style="left:66px;top:144px">
    <div class="ph" role="img" aria-label="Open dining and living area" style="background:linear-gradient(180deg,#e6e4e0,#a9a39b)"><span class="price">$638,000</span></div>
    <p class="loc">West Hollywood, CA 90069</p><h3>2451 Marlow Crest Road</h3>
    <p class="meta">3 bedrooms &nbsp;-&nbsp; 2 bathrooms &nbsp;-&nbsp; 1,554 sq. ft.</p>
    <div class="row"><span class="tag">For Sale</span><span class="pill">View Details</span></div>
  </div>
  <div class="card" style="left:430px;top:144px">
    <div class="ph" role="img" aria-label="Living room with brown leather sofa" style="background:linear-gradient(180deg,#d8dcdc,#8f7a62)"><span class="price">$20,000/m</span></div>
    <p class="loc">Los Angeles, CA 90002</p><h3>5380 Wrenfield Avenue</h3>
    <p class="meta">3 bedrooms &nbsp;-&nbsp; 2 bathrooms &nbsp;-&nbsp; 1,554 sq. ft.</p>
    <div class="row"><span class="tag">For Rent</span><span class="pill">View Details</span></div>
  </div>
  <div class="card" style="left:795px;top:144px">
    <div class="ph" role="img" aria-label="Modern white kitchen" style="background:linear-gradient(180deg,#f0efed,#b3aca3)"><span class="price">$638,000</span></div>
    <p class="loc">Los Angeles, CA 90068</p><h3>3917 Halloway Drive</h3>
    <p class="meta">3 bedrooms &nbsp;-&nbsp; 2 bathrooms &nbsp;-&nbsp; 1,554 sq. ft.</p>
    <div class="row"><span class="tag">For Sale</span><span class="pill">View Details</span></div>
  </div>
</section>

<section class="testimonials">
  <div class="ph" role="img" aria-label="Kitchen interior with bar stools, tinted teal"></div>
  <div class="t-kicker">Testimonials</div>
  <h2 class="t-title serif">What Our<br>Happy Customers<br>Say About Us</h2>
  <div class="t-arrows">
    <span><svg width="10" height="10" viewBox="0 0 10 10" fill="none" stroke="#fff" stroke-width="1.5"><path d="M6.5 1.5L3 5l3.5 3.5"/></svg></span>
    <span><svg width="10" height="10" viewBox="0 0 10 10" fill="none" stroke="#fff" stroke-width="1.5"><path d="M3.5 1.5L7 5 3.5 8.5"/></svg></span>
  </div>
  <div class="avatar" role="img" aria-label="Customer portrait"></div>
  <p class="quote">"Crescendo caeleste dixere tegit mare. Bene peregrinum recessit cinxit diremit coeperunt. Invasit habentem minantia fuerat utramque iapeto finxit."</p>
  <p class="q-by">JENNY DOE, BUYER</p>
</section>

<section class="blog">
  <h2 class="sec-title serif" style="top:114px">Latest Blog Posts</h2>
  <span class="view-all">View All Blogs</span>

  <div class="card" style="left:66px;top:184px">
    <div class="ph" role="img" aria-label="Waterfront house with pool" style="background:linear-gradient(180deg,#4c8fd0 0%,#d7dde2 55%,#5a7a8a 100%)"><span class="price">22 JUN 2024</span></div>
    <p class="cat">HOME BUYING</p><h3>Circumfluus carmen unda dissociata deerat scythiam</h3>
    <p class="excerpt">Timebat duae habitandae siccis usu. Invasit regna terra addidit di legebantur.</p>
    <span class="pill">Read More</span>
  </div>
  <div class="card" style="left:430px;top:184px">
    <div class="ph" role="img" aria-label="Kitchen with wooden cabinets" style="background:linear-gradient(180deg,#d9c6ae 0%,#9a6a42 60%,#c9c2b8 100%)"><span class="price">22 JUN 2024</span></div>
    <p class="cat">HOME SELLING</p><h3>Formas parte cetera galeae gentes mare</h3>
    <p class="excerpt">Timebat duae habitandae siccis usu. Invasit regna terra addidit di legebantur.</p>
    <span class="pill">Read More</span>
  </div>
  <div class="card" style="left:795px;top:184px">
    <div class="ph" role="img" aria-label="Suburban house with lawn" style="background:linear-gradient(180deg,#78b0e0 0%,#c9d2d0 45%,#5f8f3f 100%)"><span class="price">22 JUN 2024</span></div>
    <p class="cat">RENTING</p><h3>Quanto locavit sanctius duris amphitrite septemque</h3>
    <p class="excerpt">Timebat duae habitandae siccis usu. Invasit regna terra addidit di legebantur.</p>
    <span class="pill">Read More</span>
  </div>
</section>

<section class="video">
  <h2 class="abs h2 serif" style="top:102px;width:100%">Video Spotlight</h2>
  <p class="abs lead" style="top:152px;width:100%">UndCaeleste grandia densior peregrinum regio. Cesserunt caelumque. Vultus quae litem.</p>
  <div class="player" role="img" aria-label="Aerial video of a waterfront estate with pool and dock">
    <div class="play"><svg width="34" height="38" viewBox="0 0 34 38"><path d="M4 2l28 17L4 36z" fill="#1c2226"/></svg></div>
  </div>
</section>

<section class="newsletter">
  <h2 class="abs h2 serif" style="top:-4px;width:100%">Stay Updated. Be the First to Know.</h2>
  <p class="abs lead" style="top:50px;left:150px;width:900px">Undas obliquis effigiem amphitrite. Valles hanc. Nubes dominari imagine! Caeleste grandia densior peregrinum regio. Cesserunt caelumque. Vultus quae litem. Coercuit caeli sublime. Finxit ventis caelo rapidisque. Poena orba congeriem. Lumina umor partim hunc tepescunt! Iapeto mutatas dei duris quisquis nitidis erant terra militis.</p>
  <div class="email">
    <svg width="16" height="14" viewBox="0 0 16 14" fill="none" stroke="#1d6a80" stroke-width="1.6"><rect x="1" y="1" width="14" height="12" rx="1.5"/><path d="M1.5 2l6.5 5 6.5-5"/></svg>
    Enter email address
    <div class="go">Subscribe Now</div>
  </div>
</section>

<footer class="footer">
  <div class="f-logo"><i></i>TZ Real Estate</div>
  <div class="f-col" style="left:332px">
    <h4>CALIFORNIA OFFICE</h4>
    <p>1820 Larkspur Canyon Way,<br>Juniper Flats, CA 92011</p>
    <p>(555) 014 2298</p>
  </div>
  <div class="f-col" style="left:602px">
    <h4>CALIFORNIA OFFICE</h4>
    <p>640 Alder Ridge Lane,<br>Pinecrest Vale, CA 93120</p>
    <p>(555) 014 2298</p>
  </div>
  <div class="f-col" style="left:864px">
    <h4>SOCIAL MEDIA</h4>
    <div class="social"><span aria-label="Social link 1"></span><span aria-label="Social link 2"></span><span aria-label="Social link 3"></span><span aria-label="Social link 4"></span><span aria-label="Social link 5"></span></div>
  </div>
  <div class="f-rule"></div>
  <p class="legal">Terms of Use<em>|</em>Privacy Policy<em>|</em>Cookie Policy<em>|</em>DMCA<em>|</em>Fair Housing<em>|</em>Accessibility</p>
  <p class="f-text">Quanto locavit sanctius duris amphitrite septemque. Cuncta animalibus totidem. Piscibus spisso animalibus diffundi undas. Sponte liquidas tanta minantia orba aliis. Igni pontus magni spectent quod habendum nova. Nullus ubi ultima elementaque.</p>
  <p class="copy">Copyright © 2024 TZ Real Estate. All rights reserved.</p>
</footer>

</body>
</html>
```